Divorce marketing brochure - Which will include a toy ball and chain as a gimick

A single page marketing enclosure which includes a toy ball and chain to be given to lawyers. I want to convey the following messages:

1. We pay a 1/3 referral fee;
2. We solve difficult problems.

Examples of problems solved:
*Litigation of complex property, custody, support and parenting time issues;
*Protection (or invasion) of personal injury proceeds in divorce;
*Distribution of consortium proceeds in divorce;
*Pre-nuptial and Post-nuptial agreements.
*Settlements
*Reduce conflict

A sample of the toy ball and chain enclosure can be viewed here:

My website is www.thesplitcounsel.com (currently being updated - who's isn't?)

http://www.shopvexto.com/Orbel-Trinkets-Inc-Convict-Shackle/dp/K7QX3MZP21/ref=sr_1_9?ie=UTF8&qid=1311011554&sr=8-9

Target Market(s)

Personal Injury Attorneys

Industry/Entity Type

Marketing

Requirements
Must have
• Call to action:

www.thesplitcounsel.com
1-877-HIRE-TEAM
248-555-7182
Marcus@brevanlegal.com
Nice to have
• I want this campaign to stand out. Different is good. I am a divorce lawyer marketing to personal injury attorneys (and some others) for divorce referrals. (No one forgets the girl with red hair and braces) I want the campaign to be remembered without being offensive.
Should not have

```html
<!DOCTYPE html>
<html lang="en">
<head>
<meta charset="utf-8">
<title>We Pay a 1/3 Referral Fee</title>
<link rel="stylesheet" href="https://fonts.googleapis.com/css2?family=Anton&family=Oswald:wght@300&family=Roboto+Condensed:wght@700&family=Open+Sans:wght@400;700&display=swap">
<style>
  :root {
    --yellow: #ffec00;
    --red: #e2161d;
    --red-dark: #b70d12;
    --white: #ffffff;
    --ink: #222222;
    --grey-light: #eeeeee;
    --grey-mid: #bdbdbd;
    --steel: #2a2a2a;
  }
  * { box-sizing: border-box; margin: 0; padding: 0; }
  html, body { width: 846px; height: 1200px; overflow: hidden; background: var(--white); }
  .flyer { position: relative; width: 846px; height: 1200px; background: var(--white); overflow: hidden; }

  .headline-band {
    position: absolute; left: 0; top: 0; width: 846px; height: 296px;
    background: var(--yellow);
  }
  .headline {
    position: absolute; left: 0; top: 14px; width: 100%;
    text-align: center;
    font-family: "Anton", Impact, sans-serif;
    font-size: 122px; line-height: 124px;
    color: var(--red);
    -webkit-text-stroke: 10px var(--white);
    paint-order: stroke fill;
    text-shadow: 3px 5px 6px rgba(0,0,0,0.35);
    letter-spacing: 1px;
  }

  .promise-band {
    position: absolute; left: 0; top: 296px; width: 846px; height: 104px;
    background: var(--red);
    display: flex; align-items: center; justify-content: center;
  }
  .promise {
    font-family: "Roboto Condensed", "Arial Narrow", sans-serif;
    font-weight: 700; font-size: 52px; color: var(--white);
    letter-spacing: 0.5px;
  }

  .examples-title {
    position: absolute; left: 0; top: 414px; width: 100%;
    text-align: center;
    font-family: "Oswald", sans-serif; font-weight: 300;
    font-size: 46px; letter-spacing: 4px; color: var(--red);
  }

  .problem-list {
    position: absolute; top: 494px;
    list-style: none;
    font-family: "Roboto Condensed", "Arial Narrow", sans-serif;
    font-weight: 700; font-size: 28px; line-height: 33px; color: var(--ink);
  }
  .problem-list.left { left: 90px; width: 350px; }
  .problem-list.right { left: 456px; width: 330px; }
  .problem-list li { position: relative; padding-left: 22px; margin-bottom: 4px; }
  .problem-list li::before {
    content: ""; position: absolute; left: 2px; top: 13px;
    width: 9px; height: 9px; border-radius: 50%; background: var(--ink);
  }

  .cta-box {
    position: absolute; left: 70px; top: 704px; width: 372px; height: 200px;
    border-radius: 18px;
    background: linear-gradient(180deg, #f03a3f 0%, var(--red) 45%, var(--red-dark) 100%);
    box-shadow: 0 3px 8px rgba(0,0,0,0.3);
    padding: 18px 0 0 24px;
    font-family: "Open Sans", Arial, sans-serif; color: var(--white);
  }
  .cta-title { font-weight: 700; font-size: 29px; line-height: 36px; }
  .cta-line { font-size: 27px; line-height: 36px; }
  .cta-line.bold { font-weight: 700; }

  .brief-note {
    position: absolute; left: 456px; top: 706px; width: 340px;
    font-family: "Open Sans", Arial, sans-serif;
    font-size: 13.5px; line-height: 18px; color: var(--ink);
  }

  .ball-and-chain {
    position: absolute; left: 80px; top: 940px; width: 710px; height: 220px;
    border-radius: 24px;
    background: radial-gradient(ellipse at 82% 55%, var(--steel) 0%, #555 22%, var(--grey-light) 48%, var(--white) 75%),
                linear-gradient(90deg, var(--grey-mid) 0%, var(--grey-light) 50%, var(--white) 100%);
    background-blend-mode: multiply;
  }
</style>
</head>
<body>
<main class="flyer">
  <header class="headline-band">
    <h1 class="headline">WE PAY A 1/3<br>REFERRAL FEE</h1>
  </header>

  <div class="promise-band">
    <h2 class="promise">WE SOLVE DIFFICULT PROBLEMS</h2>
  </div>

  <h3 class="examples-title">EXAMPLES OF PROBLEMS SOLVED:</h3>

  <ul class="problem-list left">
    <li>Litigation of complex property, custody, support and parenting time issues</li>
    <li>Protection (or invasion) of personal injury proceeds in divorce</li>
  </ul>
  <ul class="problem-list right">
    <li>Distribution of consortium proceeds in divorce</li>
    <li>Pre-nuptial and Post-nuptial agreements</li>
    <li>Settlements</li>
    <li>Reduce conflict</li>
  </ul>

  <section class="cta-box">
    <p class="cta-title">CALL TO ACTION:</p>
    <p class="cta-line">www.thesplitcounsel.com</p>
    <p class="cta-line bold">1-877-HIRE-TEAM</p>
    <p class="cta-line bold">248-555-7182</p>
    <p class="cta-line">Marcus@brevanlegal.com</p>
  </section>

  <p class="brief-note">I want this campaign to stand out. Different is good. I am a divorce lawyer marketing to personal injury attorneys (and some others) for divorce referrals. (No one forgets the girl with red hair and braces) I want the campaign to be remembered without being offensive.</p>

  <div class="ball-and-chain" role="img" aria-label="Toy ball and chain: a black iron ball joined by a chain to a shackle set with a diamond ring"></div>
</main>
</body>
</html>
```